" Prestamos serviços de suporte técnico à clientes como: -gestão de TI, -instalação de rede, firewall, internet/intranet -Segurança da Informação -Auditoria de Parque de Equipamentos de TI e Segurança de dados "

```html
<!DOCTYPE html>
<html lang="pt-BR">
<head>
<meta charset="UTF-8">
<title>Pasta – Vertente &amp; Horizontes</title>
<link rel="stylesheet" href="https://fonts.googleapis.com/css2?family=Montserrat:wght@500;800&display=swap">
<style>
  :root {
    --bg: #d9dadc;
    --paper: #ffffff;
    --ink: #0b0b0c;
    --blue: #1f7fd1;
    --text-dark: #1a1a1a;
    --text-muted: #3b3b3b;
  }
  * { box-sizing: border-box; margin: 0; padding: 0; }
  html, body {
    width: 1200px; height: 1200px; overflow: hidden;
    background: var(--bg);
    font-family: "Montserrat", sans-serif;
  }
  .folder {
    position: absolute; left: 50px; top: 230px;
    width: 1100px; height: 740px;
    display: flex;
    box-shadow: 0 18px 40px rgba(0,0,0,.18);
  }
  .panel { position: relative; width: 550px; height: 740px; overflow: hidden; }
  .panel--back { background: var(--paper); }
  .panel--front { background: var(--ink); }

  .back-band {
    position: absolute; left: 0; right: 0; bottom: 18px;
    height: 12px; background: var(--blue);
  }
  .back-brand {
    position: absolute; left: 110px; top: 558px;
    font-weight: 800; font-size: 17px; color: var(--text-dark);
    width: 150px; line-height: 1.15;
  }
  .contact-list {
    position: absolute; left: 285px; top: 556px;
    list-style: none; font-size: 11.5px; font-weight: 500; color: var(--text-muted);
  }
  .contact-list li { display: flex; align-items: center; gap: 8px; height: 24px; }
  .contact-list svg { width: 12px; height: 12px; flex: none; }
  .address {
    position: absolute; left: 150px; top: 658px;
    display: flex; gap: 9px; align-items: flex-start;
    font-size: 11.5px; font-weight: 500; color: var(--text-muted); line-height: 1.4;
  }
  .address svg { width: 13px; height: 17px; flex: none; margin-top: 1px; }

  .front-accent {
    position: absolute; left: 0; top: 0; width: 550px; height: 220px;
    background: linear-gradient(200deg, rgba(31,127,209,.55) 0%, rgba(31,127,209,.18) 40%, rgba(11,11,12,0) 75%);
  }
  .front-brand {
    position: absolute; left: 0; right: 0; top: 340px;
    display: flex; align-items: center; justify-content: center; gap: 16px;
  }
  .front-brand__mark { width: 22px; height: 22px; border-radius: 50%; background: var(--blue); flex: none; }
  .front-brand__name { font-weight: 800; font-size: 38px; color: var(--paper); letter-spacing: -.5px; white-space: nowrap; }
</style>
</head>
<body>
  <main class="folder">
    <section class="panel panel--back">
      <p class="back-brand">Vertente &amp; Horizontes</p>
      <ul class="contact-list">
        <li>
          <svg viewBox="0 0 24 24" aria-hidden="true"><path fill="#1f7fd1" d="M6.6 10.8a15.5 15.5 0 0 0 6.6 6.6l2.2-2.2a1 1 0 0 1 1-.25 11.4 11.4 0 0 0 3.6.57 1 1 0 0 1 1 1V20a1 1 0 0 1-1 1A17 17 0 0 1 3 4a1 1 0 0 1 1-1h3.5a1 1 0 0 1 1 1c0 1.25.2 2.45.57 3.57a1 1 0 0 1-.25 1z"/></svg>
          (21) 9 5555-0148
        </li>
        <li>
          <svg viewBox="0 0 24 24" aria-hidden="true"><path fill="#1f7fd1" d="M6.6 10.8a15.5 15.5 0 0 0 6.6 6.6l2.2-2.2a1 1 0 0 1 1-.25 11.4 11.4 0 0 0 3.6.57 1 1 0 0 1 1 1V20a1 1 0 0 1-1 1A17 17 0 0 1 3 4a1 1 0 0 1 1-1h3.5a1 1 0 0 1 1 1c0 1.25.2 2.45.57 3.57a1 1 0 0 1-.25 1z"/></svg>
          (21) 5555-0192
        </li>
        <li>
          <svg viewBox="0 0 24 24" aria-hidden="true"><circle cx="12" cy="12" r="10" fill="#1f7fd1"/><path d="M2 12h20M12 2c3 3 3 17 0 20M12 2c-3 3-3 17 0 20" stroke="#fff" stroke-width="1.4" fill="none"/></svg>
          www.vertentehorizontes.com.br
        </li>
      </ul>
      <div class="address">
        <svg viewBox="0 0 24 32" aria-hidden="true"><path fill="#1f7fd1" d="M12 0C5.4 0 0 5.2 0 11.7 0 20.5 12 32 12 32s12-11.5 12-20.3C24 5.2 18.6 0 12 0zm0 16.5a5 5 0 1 1 0-10 5 5 0 0 1 0 10z"/></svg>
        <p>Rua das Palmeiras Azuis, 210 - Sala 804 - Centro<br>Rio de Janeiro/RJ - CEP: 20000-000</p>
      </div>
      <div class="back-band"></div>
    </section>

    <section class="panel panel--front">
      <div class="front-accent" role="img" aria-label="Decorative sweeping bands in white and blue across the top of the cover"></div>
      <div class="front-brand">
        <span class="front-brand__mark"></span>
        <span class="front-brand__name">Vertente &amp; Horizontes</span>
      </div>
    </section>
  </main>
</body>
</html>
```